Herausgeber suchen Design
Zielgruppe
Wir sind Herausgeber einer Festschrift für unseren Doktor-/Habilvater, Prof. Dr. Lohmeyer, und suchen ein hochwertiges Design für die Einladungskarten zu einem Symposium, im Rahmen dessen die Festschrift übergeben wird; Zielgruppe sind die Autoren der Festschrift, Alumnis und Weggefährten von Herrn Lohmeyer
Aufgabenstellung
- Maße: 210 mm x 105 mm
- Einladungskarte: geklappt; Frontseite, 2 Innenseiten, Rückseite
- Zum Text siehe Datei 'Text Einladungskarte'
- Design eher traditionell/konservativ, da es sich um einen wissenschaftlichen Hintergrund handelt (Symposium, Übergabe Festschrift)
- Die Farben sollen mit dem Cover der Festschrift korrespondieren (vgl. Datei 'Templates_Research_Vossek', dort das erste Cover (KLM_RE_T01)

```html
<!DOCTYPE html>
<html lang="de">
<head>
<meta charset="utf-8">
<title>Einladung – Symposium</title>
<link rel="stylesheet" href="https://fonts.googleapis.com/css2?family=Encode+Sans+Condensed:wght@400&display=swap">
<style>
  :root {
    --blue: #0366b0;
    --navy: #1f2c52;
    --white: #ffffff;
  }
  html, body {
    margin: 0;
    padding: 0;
    width: 1200px;
    height: 1200px;
    overflow: hidden;
    background: var(--navy);
  }
  .card-front {
    position: relative;
    width: 1200px;
    height: 1200px;
    overflow: hidden;
  }
  .card-front__shapes {
    position: absolute;
    inset: 0;
    display: block;
  }
  .card-front__title {
    position: absolute;
    left: 748px;
    top: 962px;
    margin: 0;
    font-family: "Encode Sans Condensed", "Arial Narrow", sans-serif;
    font-weight: 400;
    font-size: 80px;
    line-height: 1;
    letter-spacing: 0.5px;
    color: var(--white);
  }
</style>
</head>
<body>
  <main class="card-front">
    <svg class="card-front__shapes" width="1200" height="1200" viewBox="0 0 1200 1200" aria-hidden="true">
      <rect class="band-navy" x="0" y="0" width="1200" height="1200" fill="var(--navy)"/>
      <polygon class="field-blue" points="0,0 1200,0 1200,847 58,903 0,851" fill="var(--blue)"/>
      <polygon class="field-blue-left" points="0,0 57,0 57,851 0,853" fill="var(--blue)"/>
      <line class="rule-vertical" x1="57.5" y1="0" x2="57.5" y2="1121" stroke="var(--white)" stroke-width="2"/>
    </svg>
    <h1 class="card-front__title">Einladung</h1>
  </main>
</body>
</html>
```